#1 Selling Sweden weight loss supplement comes to USA - LABEL needed!

The number one weight loss in Sweden is coming to USA

-I need a label that is clean and simple but somehow represents, in an abstract way, weight loss or slender.
-The product and water mixed is all the is needed. This too could be represented in the label design.
-The bottle will be white.

-Attached is a picture of a supplement bottle with
--the logo for the company, 'NuKelvara'
--the name of the supplement, 'Kelvara Lithe'
and
--other text that could be included in the final label.

ALSO attached are 2 label designs that I like. This might give you an idea of a direction to go.
Thank You very much.

Target Market(s)

Health conscience people

Industry/Entity Type

Weight

Font styles to use
Sans Serif

Requirements
Must have
• -Size of bottle - 2" wide x 4" high
Nice to have
• *Lowers Hunger up to 50%
• *Decreases cravings or unhealthy foods up to 90%
• *Enhances Weight Loss
• " A Durovix a day keeps hunger away"

```html
<!DOCTYPE html>
<html lang="en">
<head>
<meta charset="utf-8">
<title>Kelvara Lithe – Supplement Label</title>
<link rel="stylesheet" href="https://fonts.googleapis.com/css2?family=Baloo+2:wght@800&family=Nunito:ital,wght@0,300;0,400;0,600;1,600;1,700&display=swap">
<style>
  :root {
    --canvas: #ffffff;
    --navy: #2c2f6b;
    --title-blue: #1d5f9e;
    --title-blue-deep: #123e78;
    --leaf-green: #5fae38;
    --leaf-light: #9bd45a;
    --pill-start: #a7dd63;
    --pill-end: #2f8a25;
    --pill-text: #ffffff;
    --tagline: #7cc142;
  }
  * { margin: 0; padding: 0; box-sizing: border-box; }
  html, body { width: 918px; height: 1200px; overflow: hidden; background: var(--canvas); }
  .label {
    position: relative;
    width: 918px;
    height: 1200px;
    font-family: "Nunito", sans-serif;
  }
  .brand {
    position: absolute;
    top: 150px;
    left: 0;
    width: 100%;
    display: flex;
    justify-content: center;
    align-items: center;
    gap: 18px;
  }
  .brand-name {
    font-family: "Nunito", sans-serif;
    font-weight: 400;
    font-size: 72px;
    color: var(--navy);
    letter-spacing: 1px;
  }
  .brand-dot {
    width: 34px; height: 34px;
    border-radius: 50%;
    background: var(--leaf-green);
  }
  .product-title {
    position: absolute;
    top: 330px;
    left: 0;
    width: 100%;
    text-align: center;
    font-family: "Baloo 2", sans-serif;
    font-weight: 800;
    line-height: 0.9;
  }
  .product-title .line-one {
    display: block;
    font-size: 170px;
    color: var(--title-blue);
    background: linear-gradient(180deg, #3f9ad6 0%, var(--title-blue) 45%, var(--title-blue-deep) 100%);
    -webkit-background-clip: text;
    background-clip: text;
    -webkit-text-fill-color: transparent;
    letter-spacing: -3px;
  }
  .product-title .line-two {
    display: block;
    font-size: 170px;
    color: var(--leaf-green);
    background: linear-gradient(180deg, var(--leaf-light) 0%, var(--leaf-green) 60%, #3f8c27 100%);
    -webkit-background-clip: text;
    background-clip: text;
    -webkit-text-fill-color: transparent;
    letter-spacing: -3px;
    padding-left: 90px;
  }
  .formula {
    position: absolute;
    top: 668px;
    left: 0;
    width: 100%;
    text-align: center;
    padding-left: 90px;
    font-weight: 300;
    font-size: 44px;
    letter-spacing: 3px;
    color: var(--leaf-green);
  }
  .benefits {
    position: absolute;
    top: 780px;
    left: 262px;
    list-style: none;
    display: flex;
    flex-direction: column;
    gap: 18px;
  }
  .benefit {
    background: linear-gradient(90deg, var(--pill-start) 0%, var(--pill-end) 100%);
    color: var(--pill-text);
    font-style: italic;
    font-weight: 600;
    font-size: 25px;
    line-height: 1.05;
    border-radius: 34px;
    padding: 12px 30px;
  }
  .benefit--short { width: 420px; }
  .benefit--wide { width: 540px; padding-top: 14px; padding-bottom: 14px; }
  .tagline {
    position: absolute;
    top: 1080px;
    left: 0;
    width: 100%;
    text-align: center;
    font-style: italic;
    font-weight: 700;
    font-size: 34px;
    color: var(--tagline);
  }
</style>
</head>
<body>
  <main class="label">
    <header class="brand">
      <span class="brand-name">NuKelvara</span>
      <span class="brand-dot"></span>
    </header>

    <h1 class="product-title">
      <span class="line-one">Kelvara</span>
      <span class="line-two">Lithe</span>
    </h1>

    <p class="formula">W/ PURE DUROVIX</p>

    <ul class="benefits">
      <li class="benefit benefit--short">Lowers Hunger up to 50%</li>
      <li class="benefit benefit--wide">Decreases cravings or unhealthy foods<br>up to 90%</li>
      <li class="benefit benefit--short">Enhances Weight Loss</li>
    </ul>

    <p class="tagline">A Durovix a day keeps hunger away</p>
  </main>
</body>
</html>
```